Lantern Sisters Ministries Logo/Business Card

Lantern Sisters are women full of God’s love and restorative grace, who have the desire to lead other women to embrace the beautiful creation that God intended them to be. Lantern Sisters walk together with other women alongside of God toward a life of healing, restoration and empowerment… through mentoring, spiritual guidance, temporary shelter, comprehensive care, and connections to a longer-term plan that leads to renewal and wholeness in Christ.

Lantern Sisters Ministries is an organization that embraces women and children whose lives have been affected by human trafficking, prison, foster care, homelessness, addictions, and other circumstances that prevent them from achieving their full potential in Christ Jesus. We believe that God has a unique plan and purpose for every individual. Through God’s transformational power and relationships with counselors, mentors, and others, anyone can break free from the chains and bondage of slavery, addictions and the strongholds of life.

We are just starting to brand our organization, and need both business cards and a logo. We do not have a logo yet, and would like design ideas. One of our young ladies (rescued from trafficking) has a vision of a logo with a crown with 3 ladies below/around it (representing healing, restoration, empowerment). Another lady has an idea of blending a crown, heart, and cross into the logo. We are open to creative suggestions.

Target Market(s)

Donations from churches, businesses, organizations and individuals with a passion for Trafficking and Justice

Industry/Entity Type

Business

Contact Information for Business Card

Lantern Sisters Ministries
sisters carrying the light toward healing, renewal and a stronger tomorrow (tag line - italics)

Card 1:
Marla Tibbets, Director
555.203.7718
marla@lanternsistersministries.example
www.lanternsistersministries.example (optional)

Card 2:
Rosalind Pickett, Director
555.617.4420
ros@lanternsistersministries.example

```html
<!DOCTYPE html>
<html lang="en">
<head>
<meta charset="utf-8">
<title>Lantern Sisters Ministries – Business Card</title>
<link rel="stylesheet" href="https://fonts.googleapis.com/css2?family=Questrial&family=EB+Garamond:ital,wght@1,400&display=swap">
<style>
  :root {
    --ink-dark: #141414;
    --ink-dark-edge: #262a2a;
    --paper: #ffffff;
    --magenta: #d23ad0;
    --grey-light: #c9c9c9;
    --swoosh-light: #d9dcdc;
    --swoosh-dark: #6e7474;
    --tag-dark: #111111;
    --brand-ink: #2a2d2d;
  }
  html, body {
    margin: 0;
    padding: 0;
    width: 1200px;
    height: 702px;
    overflow: hidden;
    background: var(--paper);
  }
  .card {
    position: relative;
    width: 1200px;
    height: 702px;
    overflow: hidden;
  }
  .card-art {
    position: absolute;
    inset: 0;
  }
  .contact {
    position: absolute;
    left: 0;
    top: 0;
    width: 640px;
    font-family: "Questrial", "Century Gothic", sans-serif;
    text-align: center;
  }
  .contact-name {
    position: absolute;
    left: 0; width: 640px;
    top: 186px;
    margin: 0;
    font-size: 39px;
    font-weight: 400;
    letter-spacing: 1.5px;
    color: var(--magenta);
  }
  .contact-role {
    position: absolute;
    left: 0; width: 640px;
    top: 232px;
    margin: 0;
    font-size: 24px;
    letter-spacing: 1.5px;
    color: var(--grey-light);
  }
  .contact-phone {
    position: absolute;
    left: 0; width: 640px;
    top: 340px;
    margin: 0;
    font-size: 40px;
    letter-spacing: 3px;
    color: var(--magenta);
  }
  .contact-links {
    position: absolute;
    left: 0; width: 680px;
    top: 444px;
    margin: 0;
    font-size: 23px;
    line-height: 34px;
    letter-spacing: 1.2px;
    color: var(--grey-light);
  }
  .brand {
    position: absolute;
    left: 700px;
    top: 250px;
    width: 440px;
    display: flex;
    align-items: center;
    gap: 22px;
  }
  .brand-dot {
    flex: none;
    width: 46px;
    height: 46px;
    border-radius: 50%;
    background: var(--magenta);
  }
  .brand-name {
    margin: 0;
    font-family: "Questrial", "Century Gothic", sans-serif;
    font-weight: 400;
    font-size: 40px;
    line-height: 50px;
    letter-spacing: 1.5px;
    color: var(--brand-ink);
  }
  .tagline-text {
    font-family: "EB Garamond", Georgia, serif;
    font-style: italic;
    font-size: 30px;
    letter-spacing: 1.8px;
  }
</style>
</head>
<body>
<main class="card">
  <svg class="card-art" width="1200" height="702" viewBox="0 0 1200 702" aria-hidden="true">
    <defs>
      <linearGradient id="dark-panel" x1="0" y1="0" x2="1" y2="0">
        <stop offset="0" stop-color="var(--ink-dark)"/>
        <stop offset="1" stop-color="var(--ink-dark-edge)"/>
      </linearGradient>
      <linearGradient id="swoosh" x1="0" y1="0" x2="0" y2="1">
        <stop offset="0" stop-color="var(--swoosh-light)"/>
        <stop offset="0.6" stop-color="var(--swoosh-dark)"/>
        <stop offset="1" stop-color="var(--swoosh-dark)" stop-opacity="0"/>
      </linearGradient>
      <clipPath id="light-side">
        <path d="M640 0 C585 160 580 430 800 702 L1200 702 L1200 0 Z"/>
      </clipPath>
    </defs>
    <rect class="dark-panel" width="1200" height="702" fill="url(#dark-panel)"/>
    <path class="swoosh" d="M612 0 C560 170 572 410 660 540 C612 410 600 200 672 0 Z" fill="url(#swoosh)"/>
    <path class="light-panel" d="M640 0 C585 160 580 430 800 702 L1200 702 L1200 0 Z" fill="var(--paper)"/>
    <text class="tagline-text" x="605" y="643" text-anchor="middle" fill="var(--paper)">sisters carrying the light toward healing, renewal and a stronger tomorrow</text>
    <g clip-path="url(#light-side)">
      <text class="tagline-text" x="605" y="643" text-anchor="middle" fill="var(--tag-dark)">sisters carrying the light toward healing, renewal and a stronger tomorrow</text>
    </g>
  </svg>

  <section class="contact">
    <h1 class="contact-name">Marla Tibbets</h1>
    <p class="contact-role">Director</p>
    <p class="contact-phone">555.203.7718</p>
    <p class="contact-links">www.lanternsistersministries.example<br>marla@lanternsistersministries.example</p>
  </section>

  <div class="brand">
    <span class="brand-dot" aria-hidden="true"></span>
    <p class="brand-name">Lantern Sisters<br>Ministries</p>
  </div>
</main>
</body>
</html>
```